Business Card Design Project

I want a design for my business cards based on an excisting logo design.

Target Market(s)

Marketeers, PR-peeps, CEO's, decisionmakers, entrepreneurs

Industry/Entity Type

Business

Requirements
Nice to have
• Some visual interest on the back too
Should not have
• Sarif on the font

```html
<!DOCTYPE html>
<html lang="nl">
<head>
<meta charset="utf-8">
<title>Leafwise PR – visitekaartje</title>
<link rel="stylesheet" href="https://fonts.googleapis.com/css2?family=Open+Sans:wght@300;400;700&display=swap">
<style>
  :root {
    --leaf-green: #a5cd39;
    --mark-green: #86b52a;
    --card-white: #ffffff;
    --ink-grey: #4d4d4d;
    --brand-grey: #8c8c8c;
    --icon-grey: #6b6b6b;
    --backdrop: #e8e5e0;
  }
  * { margin: 0; padding: 0; box-sizing: border-box; }
  html, body {
    width: 1200px; height: 758px; overflow: hidden;
    background: var(--backdrop);
    font-family: "Open Sans", Arial, sans-serif;
  }
  .canvas { position: relative; width: 1200px; height: 758px; }

  .card {
    position: absolute; top: 224px;
    width: 500px; height: 310px;
    border-radius: 24px; overflow: hidden;
    box-shadow: 0 10px 26px rgba(0,0,0,.18);
  }
  .card--front { left: 60px; background: var(--card-white); }
  .card--back  { left: 640px; background: var(--leaf-green); color: var(--card-white); }

  .front-band { position: absolute; inset: 0; }

  .holder-name {
    position: absolute; left: 300px; top: 26px;
    font-weight: 700; font-size: 17px; letter-spacing: 1.2px;
    color: var(--card-white);
  }

  .brand-dot {
    position: absolute; left: 58px; top: 56px;
    width: 116px; height: 116px; border-radius: 50%;
    background: var(--mark-green);
  }
  .brand-name {
    position: absolute; left: 38px; top: 192px;
    font-weight: 300; font-size: 31px; color: var(--brand-grey);
  }

  .contact-list {
    position: absolute; left: 300px; top: 106px;
    list-style: none; font-size: 12.5px; color: var(--ink-grey);
  }
  .contact-list li { display: flex; align-items: center; height: 20px; white-space: nowrap; }
  .contact-list svg { width: 10px; height: 10px; margin-right: 5px; flex: none; }
  .social-square { width: 9px; height: 9px; margin-right: 6px; background: var(--icon-grey); border-radius: 2px; flex: none; }

  .address {
    position: absolute; left: 318px; top: 222px;
    font-style: normal; font-size: 13px; line-height: 21px; color: var(--ink-grey);
  }

  .back-brand {
    position: absolute; top: 80px; left: 0; right: 0;
    display: flex; justify-content: center; align-items: center; gap: 14px;
  }
  .back-dot { width: 56px; height: 56px; border-radius: 50%; background: var(--card-white); }
  .back-name { font-weight: 300; font-size: 30px; color: var(--card-white); }

  .tagline {
    position: absolute; top: 176px; left: 0; right: 0;
    text-align: center; font-size: 16px; line-height: 23px;
  }
  .back-url {
    position: absolute; top: 250px; left: 0; right: 0;
    text-align: center; font-size: 17px; letter-spacing: 3px;
  }
</style>
</head>
<body>
<main class="canvas">

  <section class="card card--front" aria-label="Voorkant visitekaartje">
    <svg class="front-band" width="500" height="310" viewBox="0 0 500 310" aria-hidden="true">
      <polygon points="0,0 500,0 500,62 0,150" fill="var(--leaf-green)"/>
    </svg>

    <div class="brand-dot" aria-hidden="true"></div>
    <div class="brand-name">Leafwise PR</div>

    <div class="holder-name">Mara Jansen</div>

    <ul class="contact-list">
      <li>
        <svg viewBox="0 0 10 10" aria-hidden="true"><path d="M2 1 L4 1 L4.6 3.2 L3.4 4 Q4.3 5.8 6 6.6 L6.8 5.4 L9 6 L9 8 Q8.6 9 7.5 9 Q1 8.2 1 2.5 Q1 1.4 2 1 Z" fill="var(--icon-grey)"/></svg>
        +31(0)6 20481937
      </li>
      <li>
        <svg viewBox="0 0 10 10" aria-hidden="true"><rect x="0.5" y="2" width="9" height="6.5" fill="var(--icon-grey)"/><path d="M0.5 2 L5 5.6 L9.5 2" stroke="#fff" stroke-width="0.9" fill="none"/></svg>
        mara.jansen@leafwisepr.nl
      </li>
      <li>
        <svg viewBox="0 0 10 10" aria-hidden="true"><circle cx="5" cy="5" r="4.5" fill="var(--icon-grey)"/><path d="M0.5 5 H9.5 M5 0.5 Q2.2 5 5 9.5 M5 0.5 Q7.8 5 5 9.5" stroke="#fff" stroke-width="0.7" fill="none"/></svg>
        www.leafwisepr.nl
      </li>
      <li><span class="social-square" aria-hidden="true"></span>linkhub.nl/_leafwisepr</li>
      <li><span class="social-square" aria-hidden="true"></span>pageboard.nl/leafwisepr</li>
    </ul>

    <address class="address">
      Lindelaan 42<br>
      6701 AB Wageningen
    </address>
  </section>

  <section class="card card--back" aria-label="Achterkant visitekaartje">
    <div class="back-brand">
      <span class="back-dot" aria-hidden="true"></span>
      <span class="back-name">Leafwise PR</span>
    </div>
    <p class="tagline">
      Systemisch en strategisch PR-<br>
      marketing- en communicatieadvies
    </p>
    <p class="back-url">www.leafwisepr.nl</p>
  </section>

</main>
</body>
</html>
```